Webdesign für Versicherungsmakler
Zielgruppe
Wir sind ein Versicherungsmakler und wollen unseren Internetauftritt modernisieren. Unsere Zielgruppe sind mittelständische Unternehmen. Wir erstellen neben den Sachversicherungen und der Altersvororge auch versicherungsmathematische Gutachten. Wir beraten, erstellen Angebote und verwalten und betreuen die Versicherungsverträge und Schadenfälle unserer Kunden.
Aufgabenstellung
Es besteht bereits eine Website: https://www.k-und-r.example/. An dieser sollte sich orientiert werden, die Inhalte werden vermutlich in Zukunft Ähnlich bleiben.
Der Aufbau der Website soll modernisiert werden. Das Logo soll erhalten bleiben. Die Seite soll einen modernen, cleanen und dennoch zuverlässigen Eindruck vermitteln.

```html
<!DOCTYPE html>
<html lang="de">
<head>
<meta charset="utf-8">
<title>Kessler &amp; Rohde – Versicherungsmakler für Unternehmen</title>
<link rel="stylesheet" href="https://fonts.googleapis.com/css2?family=Nunito+Sans:wght@300;400;600;700;800&display=swap">
<style>
:root{
  --blue:#0a5a96;
  --blue-dark:#064d83;
  --accent:#e07a5f;
  --bg:#f5f3f0;
  --card:#ffffff;
  --field:#ece8e4;
  --text:#4a4a4a;
  --muted:#777;
  --line:#d9d5d0;
}
*{box-sizing:border-box;margin:0;padding:0}
html,body{width:1200px;height:3461px;overflow:hidden}
body{position:relative;background:var(--bg);font-family:"Nunito Sans",sans-serif;color:var(--text)}
.abs{position:absolute}
.brand{display:flex;align-items:center;gap:12px;color:var(--blue);font-weight:700;font-size:26px;letter-spacing:.5px}
.brand .mark{width:40px;height:40px;background:var(--blue);border-radius:4px}
.nav{left:386px;top:38px;display:flex;gap:31px;font-size:19px;color:var(--blue)}
.nav .active{color:var(--accent)}
.btn{background:var(--blue);color:#fff;font-weight:700;border-radius:4px;display:flex;align-items:center;justify-content:center;letter-spacing:.5px}
.hero-title{left:56px;top:160px;color:var(--blue);font-size:35px;font-weight:300;line-height:1.3}
.hero-title strong{display:block;font-size:39px;font-weight:800;padding-left:12px;margin-top:2px}
.hero-text{left:66px;top:264px;font-size:13px;line-height:24.5px;white-space:nowrap}
.hero-glow{left:740px;top:90px;width:420px;height:420px;border-radius:50%;background:radial-gradient(circle,rgba(224,122,95,.28),rgba(224,122,95,0) 65%)}
.hero-photo{left:833px;top:159px;width:266px;height:266px;border:4px solid #fff;border-radius:70px 0 0 0;background:linear-gradient(160deg,#b9cbe0,#5d7fa6 55%,#dfe6ee)}
.hero-badge{left:743px;top:356px;width:203px;height:53px;background:#fff;border-radius:8px;box-shadow:0 4px 14px rgba(0,0,0,.1);display:flex;align-items:center;gap:10px;padding-left:12px;color:var(--blue);font-size:13px;font-weight:600;line-height:17px;text-align:center}
.dots{left:1034px;top:498px;display:flex;align-items:center;gap:6px}
.dots i{width:7px;height:7px;border-radius:50%;background:#c9d6e4;display:block}
.dots i.on{background:var(--blue)}
.center{left:0;width:1200px;text-align:center}
.h2{color:var(--blue);font-weight:800;font-size:19px}
.small{font-size:10.5px;line-height:17px;color:#555}
.eyebrow{font-size:9px;color:var(--accent);letter-spacing:.3px}
.card{top:637px;width:309px;height:266px;background:var(--card);border:1px solid #e4e0db;border-radius:4px;text-align:center;color:var(--blue);font-weight:700;font-size:17px}
.card .art{width:150px;height:130px;margin:48px auto 0;border-radius:10px;background:linear-gradient(135deg,#dbe7f2,#f6dcd3)}
.card p{margin-top:24px;line-height:23px}
.band{left:0;top:976px;width:1200px;height:438px;background:var(--blue);color:#fff}
.band-logo{left:213px;top:1078px;width:160px;text-align:center}
.band-logo .mark{width:160px;height:152px;background:#fff;border-radius:4px 40px 4px 4px;margin-bottom:22px}
.band-logo span{font-size:25px;letter-spacing:1.5px;line-height:28px;display:block}
.band-copy{left:619px;top:1024px;width:450px}
.band-copy h3{font-size:19px;font-weight:600;margin-bottom:15px}
.band-copy p{font-size:9px;line-height:12.5px;margin-bottom:11px}
.band-copy blockquote{font-size:17.5px;font-weight:800;line-height:25px;margin-top:18px}
.member{top:1620px;width:200px;text-align:center}
.member .photo{width:174px;height:174px;border-radius:50%;margin:0 auto;background:radial-gradient(circle at 50% 40%,#cfcac4,#9a958f)}
.member h4{color:var(--blue);font-weight:600;font-size:20px;margin-top:12px;white-space:nowrap}
.member .role{font-size:14px;color:#444}
.socials{display:flex;justify-content:center;gap:5px;margin-top:6px}
.socials i{width:21px;height:21px;border-radius:50%;background:var(--blue);display:block}
.arrow-btn{width:32px;height:32px;border-radius:50%;background:#fff;box-shadow:0 2px 8px rgba(0,0,0,.12);display:flex;align-items:center;justify-content:center}
.office{top:2086px;width:230px;font-size:10px;line-height:14px;color:#555}
.office h5{color:var(--blue);font-size:14px;font-weight:700;margin:0 0 10px 0}
.office .row{display:flex;gap:8px;align-items:flex-start;margin-bottom:1px}
.office svg{flex:none;margin-top:1px}
.map{left:0;top:2279px;width:1200px;height:424px;background:linear-gradient(135deg,#e6e6e6,#d4d4d4 60%,#e2e2e2)}
.field{background:var(--field);border-radius:8px;font-size:10px;color:#666;padding:11px 18px}
.footer{left:0;top:3100px;width:1200px;height:361px;background:var(--blue);color:#fff}
.footer h6{font-size:12px;font-weight:400;margin-bottom:19px}
.footer .col{position:absolute;top:127px;font-size:10px;line-height:19px}
.footer .col a{color:#fff;text-decoration:none;display:block}
.news{display:flex;margin-top:12px}
.news span{width:215px;height:28px;background:#fff;border-radius:8px 0 0 8px;color:var(--accent);font-size:9px;padding:7px 12px}
.news b{width:98px;height:28px;background:var(--accent);border-radius:0 8px 8px 0;font-size:7px;display:flex;align-items:center;justify-content:center;font-weight:600}
.footer .rule{position:absolute;left:234px;top:269px;width:732px;height:1px;background:rgba(255,255,255,.55)}
.legal{position:absolute;left:234px;top:292px;display:flex;gap:20px;font-size:9px}
.copy{position:absolute;left:228px;top:326px;font-size:8.5px}
.foot-social{position:absolute;left:854px;top:295px;display:flex;gap:4px}
.foot-social i{width:21px;height:21px;border-radius:50%;background:#fff;display:block}
</style>
</head>
<body>

<header>
  <div class="abs brand" style="left:56px;top:31px"><span class="mark"></span>Kessler &amp; Rohde</div>
  <nav class="abs nav">
    <span class="active">Home</span><span>Profil</span><span>Dienstleistungen</span><span>Unternehmen</span><span>Service</span>
  </nav>
  <div class="abs btn" style="left:980px;top:36px;width:121px;height:33px;font-size:16px">Kontakt</div>
</header>

<section class="hero">
  <h1 class="abs hero-title">Versicherungsmakler<strong>für Unternehmen</strong></h1>
  <p class="abs hero-text">is simply dummy text of the printing and typesetting industry.<br>Lorem Ipsum has been the industry’s standard dummy text<br>ever since the 1500s, when an unknown printer took a galley of<br>type and scrambled it to make a type specimen book. It has<br>survived not only five centuries, but also the leap into electronic</p>
  <div class="abs btn" style="left:66px;top:402px;width:121px;height:31px;font-size:15px">Kontakt</div>
  <div class="abs hero-glow"></div>
  <div class="abs hero-photo" role="img" aria-label="Foto: modernes, geschwungenes Bürohochhaus aus Glas"></div>
  <div class="abs hero-badge">
    <svg width="26" height="30" viewBox="0 0 26 30"><path d="M13 2 L23 6 V14 C23 21 18 26 13 28 C8 26 3 21 3 14 V6 Z" fill="none" stroke="#e07a5f" stroke-width="2"/></svg>
    <span>Versicherungsmakler<br>für Unternehmen</span>
  </div>
  <div class="abs dots">
    <svg width="12" height="20" viewBox="0 0 12 20"><path d="M10 2 L2 10 L10 18" fill="none" stroke="#0a5a96" stroke-width="2.5"/></svg>
    <i class="on"></i><i></i><i></i>
    <svg width="12" height="20" viewBox="0 0 12 20"><path d="M2 2 L10 10 L2 18" fill="none" stroke="#0a5a96" stroke-width="2.5"/></svg>
  </div>
</section>

<section class="services">
  <h2 class="abs center h2" style="top:544px">Willkommen bei Kessler &amp; Rohde</h2>
  <p class="abs center small" style="top:581px;font-size:9.5px">Experten für Ihr Versicherungsmanagement und betriebliche Altersversorgung<br>unabhängiger Versicherungsmakler</p>
  <div class="abs card" style="left:128px"><div class="art" role="img" aria-label="Illustration: Lupe mit Zahnrad, Kalender und Schutzschild"></div><p>Versicherungsmanagement</p></div>
  <div class="abs card" style="left:457px"><div class="art" role="img" aria-label="Illustration: Checkliste mit älterer Person am Stock"></div><p>Altersvorsorge</p></div>
  <div class="abs card" style="left:786px"><div class="art" role="img" aria-label="Illustration: Balkendiagramm mit Pfeil, Haus, Karte und Schutzschild"></div><p>Versicherungsmathematische<br>Gutachten</p></div>
</section>

<section class="abs band"></section>
<div class="abs band-logo" style="color:#fff">
  <div class="mark"></div>
  <span>KESSLER<br>&amp; ROHDE</span>
</div>
<div class="abs band-copy" style="color:#fff">
  <h3>Warum Kessler und Rohde?</h3>
  <p>Wir sind Ihr Partner, um Ihren Visionen, ob als Unternehmer oder Privatperson, nachhaltig Sicherheit zu geben.</p>
  <p>Sie haben Verantwortung für Ihr Unternehmen und wissen, es gibt Risiken, die Ihre Kunden, Ihre Mitarbeiter und Sie gefährden. Ein kluges Risikomanagement ist erforderlich.</p>
  <p>Ein Teil dieses Risikomanagements ist die Absicherung durch ein gut konzeptioniertes Versicherungspaket. Nur dafür schon den Überblick zu behalten, erfordert Sachverstand, Markt- und Branchenkenntnis. Die notwendige Zeit dafür haben Sie wahrscheinlich nicht.</p>
  <p>Mit versicherungsmathematischem Sachverstand übernehmen wir unabhängig von Versicherungsgesellschaften Ihr Versicherungs- und Vorsorgemanagement. Dabei können Sie auf unsere langjährige Erfahrung setzen.</p>
  <p>Der Service macht den Unterschied. Wir wollen, dass Sie sich zu jederzeit bei uns gut aufgehoben fühlen. Neben der Beratung zählt auch die Zuverlässigkeit und Hilfe im Schadenfall. Dabei ist es unser Ziel, zur Zufriedenheit unserer Mandanten zu handeln.</p>
  <blockquote>„Unser Qualitätsanspruch ist Ihre Sicherheit - seit mehr<br>als einem Vierteljahrhundert“</blockquote>
</div>

<section class="team">
  <p class="abs center eyebrow" style="top:1486px">OUR TEAM</p>
  <h2 class="abs center h2" style="top:1502px">Meet the Team</h2>
  <p class="abs center small" style="top:1531px">Vestibulum sollicitudin nunc in eros a justo facilisis rutrum. Aenean id ullamcorper libero.<br>Vestibulum imperdiet nibh tortor mauris</p>
  <svg class="abs" style="left:118px;top:1702px" width="12" height="10" viewBox="0 0 12 10"><path d="M11 5 H2 M5 1 L1 5 L5 9" fill="none" stroke="#0a5a96" stroke-width="1.5"/></svg>
  <div class="abs arrow-btn" style="left:1063px;top:1697px"><svg width="10" height="10" viewBox="0 0 12 10"><path d="M1 5 H10 M7 1 L11 5 L7 9" fill="none" stroke="#0a5a96" stroke-width="1.5"/></svg></div>
  <div class="abs member" style="left:182px"><div class="photo" role="img" aria-label="Porträtfoto Martin Kessler"></div><h4>Martin Kessler</h4><p class="role">Geschäftsführer</p><div class="socials"><i></i><i></i><i></i></div></div>
  <div class="abs member" style="left:399px"><div class="photo" role="img" aria-label="Porträtfoto Klaus-Peter Rohde"></div><h4>Klaus-Peter Rohde</h4><p class="role">Geschäftsführung</p><div class="socials"><i></i><i></i><i></i></div></div>
  <div class="abs member" style="left:615px"><div class="photo" role="img" aria-label="Porträtfoto Sabine Lorenz"></div><h4>Sabine Lorenz</h4><p class="role">Gutachterin</p><div class="socials"><i></i><i></i><i></i></div></div>
  <div class="abs member" style="left:831px"><div class="photo" role="img" aria-label="Porträtfoto Dr. Werner Albrecht"></div><h4>Dr. Werner Albrecht</h4><p class="role">Berater</p><div class="socials"><i></i><i></i><i></i></div></div>
</section>

<section class="contact">
  <p class="abs center eyebrow" style="top:1950px">Kontakt</p>
  <h2 class="abs center h2" style="top:1965px">Wir sind für Sie Da</h2>
  <p class="abs center small" style="top:1995px">Vestibulum sollicitudin nunc in eros a justo facilisis rutrum. Aenean id ullamcorper libero.<br>Vestibulum imperdiet nibh tortor mauris</p>
  <div class="abs office" style="left:237px">
    <h5 style="margin-left:8px">Musterstadt</h5>
    <div class="row"><svg width="12" height="13" viewBox="0 0 12 13"><circle cx="6" cy="5" r="4" fill="none" stroke="#e07a5f"/><path d="M1 12 C3 9 9 9 11 12" fill="none" stroke="#e07a5f"/></svg><span>Kessler &amp; Rohde GmbH<br>Lindenallee 8<br>14480 Musterstadt</span></div>
    <div class="row"><svg width="12" height="12" viewBox="0 0 12 12"><path d="M2 1 L4 1 L5 4 L3.5 5 C4.5 7 5 7.5 7 8.5 L8 7 L11 8 L11 10 C6 11 1 6 2 1Z" fill="none" stroke="#e07a5f"/></svg><span>0300 • 5 00 12 - 0</span></div>
    <div class="row"><svg width="12" height="12" viewBox="0 0 12 12"><rect x="2" y="4" width="8" height="7" fill="none" stroke="#e07a5f"/><rect x="4" y="1" width="4" height="3" fill="none" stroke="#e07a5f"/></svg><span>0300 • 5 00 12 - 0</span></div>
    <div class="row"><svg width="12" height="12" viewBox="0 0 12 12"><rect x="1" y="3" width="10" height="7" fill="none" stroke="#e07a5f"/><path d="M1 3 L6 7 L11 3" fill="none" stroke="#e07a5f"/></svg><span>0300 • 5 00 12 - 0</span></div>
  </div>
  <div class="abs office" style="left:508px">
    <h5 style="margin-left:8px">Musterstadt</h5>
    <div class="row"><svg width="12" height="13" viewBox="0 0 12 13"><circle cx="6" cy="5" r="4" fill="none" stroke="#e07a5f"/><path d="M1 12 C3 9 9 9 11 12" fill="none" stroke="#e07a5f"/></svg><span>Kessler &amp; Rohde GmbH<br>Lindenallee 8<br>14480 Musterstadt</span></div>
    <div class="row"><svg width="12" height="12" viewBox="0 0 12 12"><path d="M2 1 L4 1 L5 4 L3.5 5 C4.5 7 5 7.5 7 8.5 L8 7 L11 8 L11 10 C6 11 1 6 2 1Z" fill="none" stroke="#e07a5f"/></svg><span>0300 • 5 00 12 - 0</span></div>
    <div class="row"><svg width="12" height="12" viewBox="0 0 12 12"><rect x="2" y="4" width="8" height="7" fill="none" stroke="#e07a5f"/><rect x="4" y="1" width="4" height="3" fill="none" stroke="#e07a5f"/></svg><span>0300 • 5 00 12 - 0</span></div>
    <div class="row"><svg width="12" height="12" viewBox="0 0 12 12"><rect x="1" y="3" width="10" height="7" fill="none" stroke="#e07a5f"/><path d="M1 3 L6 7 L11 3" fill="none" stroke="#e07a5f"/></svg><span>0300 • 5 00 12 - 0</span></div>
  </div>
  <div class="abs office" style="left:758px">
    <h5 style="margin-left:8px">Musterstadt</h5>
    <div class="row"><svg width="12" height="13" viewBox="0 0 12 13"><circle cx="6" cy="5" r="4" fill="none" stroke="#e07a5f"/><path d="M1 12 C3 9 9 9 11 12" fill="none" stroke="#e07a5f"/></svg><span>Kessler &amp; Rohde GmbH<br>Lindenallee 8<br>14480 Musterstadt</span></div>
    <div class="row"><svg width="12" height="12" viewBox="0 0 12 12"><path d="M2 1 L4 1 L5 4 L3.5 5 C4.5 7 5 7.5 7 8.5 L8 7 L11 8 L11 10 C6 11 1 6 2 1Z" fill="none" stroke="#e07a5f"/></svg><span>0300 • 5 00 12 - 0</span></div>
    <div class="row"><svg width="12" height="12" viewBox="0 0 12 12"><rect x="2" y="4" width="8" height="7" fill="none" stroke="#e07a5f"/><rect x="4" y="1" width="4" height="3" fill="none" stroke="#e07a5f"/></svg><span>0300 • 5 00 12 - 0</span></div>
    <div class="row"><svg width="12" height="12" viewBox="0 0 12 12"><rect x="1" y="3" width="10" height="7" fill="none" stroke="#e07a5f"/><path d="M1 3 L6 7 L11 3" fill="none" stroke="#e07a5f"/></svg><span>0300 • 5 00 12 - 0</span></div>
  </div>
</section>

<div class="abs map" role="img" aria-label="Stadtplan mit Standortmarkierung"></div>

<section class="message">
  <p class="abs center eyebrow" style="top:2757px;font-size:7.5px;font-weight:700">SEND US A MESSAGE</p>
  <h2 class="abs center h2" style="top:2777px">Get in touch with us</h2>
  <p class="abs center small" style="top:2812px;font-size:11px;color:#888">Vestibulum sollicitudin nunc in eros a justo facilisis rutrum. Aenean id<br>ullamcorper libero. Vestibulum imperdiet nibh tortor mauris</p>
  <div class="abs field" style="left:234px;top:2891px;width:357px;height:27px;padding-top:7px">Name</div>
  <div class="abs field" style="left:234px;top:2939px;width:169px;height:27px;padding-top:7px">Phone number</div>
  <div class="abs field" style="left:422px;top:2939px;width:169px;height:27px;padding-top:7px">Email</div>
  <div class="abs field" style="left:609px;top:2891px;width:356px;height:74px;color:#999">Your message</div>
  <div class="abs btn" style="left:540px;top:2984px;width:120px;height:31px;font-size:9px;font-weight:400;border-radius:6px;background:linear-gradient(#2f7fc0,#0a5a96);box-shadow:0 4px 10px rgba(10,90,150,.3)">SEND TO US</div>
</section>

<footer class="abs footer">
  <div style="position:absolute;left:235px;top:38px;display:flex;align-items:center;gap:8px;font-size:11px;font-weight:700"><span style="width:22px;height:22px;background:#fff;border-radius:3px;display:block"></span>Kessler &amp; Rohde</div>
  <div class="col" style="left:234px;width:160px">
    <h6>Contact Us</h6>
    <p>Beispielweg 12, 10115<br>Musterstadt</p>
    <p style="margin-top:5px">+49 300 555 0100</p>
    <p style="margin-top:5px">info@k-und-r.example</p>
  </div>
  <div class="col" style="left:421px">
    <h6>Extra links</h6>
    <a>About</a><a>News</a><a>Contacts</a><a>Testimonials</a>
  </div>
  <div class="col" style="left:528px;top:161px">
    <a>Services</a><a>Careers</a><a>Our team</a><a>Our approach</a>
  </div>
  <div class="col" style="left:652px">
    <h6>Email Newsletters</h6>
    <p>Keep me up to date with content, updates, and offers from Kessler &amp; Rohde.</p>
    <div class="news"><span>Email address</span><b>SUBSCRIBE</b></div>
  </div>
  <div class="rule"></div>
  <div class="legal"><span>Privacy Policy</span><span>Terms and Conditions</span><span>Help</span><span>Partners</span></div>
  <p class="copy">© 2025 - All Rights Reserved.</p>
  <div class="foot-social"><i></i><i></i><i></i></div>
</footer>

</body>
</html>
```